One-Page Flat Design for SEO Company [2 DAYS]

We need a one-page flat design for our SEO company. Our current website is http://www.rankloft.com/. We are looking to completely re-design the site using new flat design techniques.
Below are some examples of the type of style we're going after:
http://quormel.com/
http://tobyrand.co.uk/
https://pentaly.co/
http://milesporter.me/
As you can see- flat, clean, minimal. It is very important you follow this type of style.
For colour scheme, you may use one of the pre-made colour palettes from here:
http://www.vornacle.com/blog/inspiration/24-flat-designs-with-compelling-color-palettes
I've attached a wireframe to be followed.
Hi,

```html
<!DOCTYPE html>
<html lang="en">
<head>
<meta charset="utf-8">
<title>RankLoft – Our Services</title>
<link href="https://fonts.googleapis.com/css2?family=Open+Sans:wght@300;400;600;700&display=swap" rel="stylesheet">
<style>
  :root {
    --ink: #555555;
    --ink-dark: #333333;
    --accent: #f28a1a;
    --accent-head: #f58a1f;
    --label: #f7931e;
    --cell: #fcdca0;
    --cell-alt: #fde5b6;
    --price: #f5a11c;
    --page: #ffffff;
    --floor: #f2f2f2;
    --tick: #7bbf3a;
    --top-btn: #555555;
  }
  * { box-sizing: border-box; margin: 0; padding: 0; }
  html, body { width: 1200px; height: 839px; overflow: hidden; }
  body {
    font-family: "Open Sans", Arial, sans-serif;
    background: linear-gradient(var(--page) 0, var(--page) 810px, var(--floor) 810px);
    color: var(--ink);
    position: relative;
  }
  .services { position: absolute; inset: 0; }
  .services-title {
    position: absolute; top: 18px; left: 0; width: 100%;
    text-align: center; font-weight: 300; font-size: 42px; letter-spacing: 1px;
    color: var(--ink);
  }
  .services-rule {
    position: absolute; top: 72px; left: 574px; width: 52px; height: 4px;
    background: var(--accent);
  }
  .services-lead {
    position: absolute; top: 95px; left: 0; width: 100%;
    text-align: center; font-size: 18px; color: #666; letter-spacing: .3px;
  }
  .plan-title {
    position: absolute; top: 180px; left: 0; width: 100%;
    text-align: center; font-size: 18px; color: #666;
  }
  .plan {
    position: absolute; top: 240px; left: 78px;
    display: grid;
    grid-template-columns: 270px 188px 173px 165px 204px;
    grid-auto-rows: 43px;
    grid-template-rows: 53px;
    column-gap: 5px; row-gap: 2px;
  }
  .plan-head {
    background: var(--accent-head); color: #fff; font-size: 14px; font-weight: 600;
    display: flex; align-items: flex-end; padding: 0 0 8px 8px;
  }
  .plan-head.blank { background: transparent; }
  .plan-label {
    background: var(--label); color: #fff; font-size: 14px; font-weight: 700;
    display: flex; align-items: center; padding-left: 12px;
  }
  .plan-cell {
    background: var(--cell); font-size: 14px; color: var(--ink);
    display: flex; align-items: center; justify-content: center;
  }
  .plan-cell.alt { background: var(--cell-alt); }
  .plan-price-label {
    font-size: 14px; font-weight: 700; color: var(--ink-dark);
    display: flex; align-items: flex-start; padding-top: 8px;
  }
  .plan-price {
    font-size: 34px; font-weight: 700; color: var(--price);
    display: flex; align-items: center; justify-content: center; padding-top: 14px;
  }
  .back-to-top {
    position: absolute; left: 1134px; top: 496px; width: 48px; height: 48px;
  }
</style>
</head>
<body>
<section class="services">
  <h1 class="services-title">OUR SERVICES</h1>
  <div class="services-rule"></div>
  <p class="services-lead">AT RANKLOFT.COM, WE OFFER A VARIETY OF SEO SERVICES.</p>
  <h2 class="plan-title" style="font-weight:400">OUR PLAN</h2>

  <div class="plan">
    <div class="plan-head blank"></div>
    <div class="plan-head">Bronze Package</div>
    <div class="plan-head">Silver Package</div>
    <div class="plan-head">Gold Package</div>
    <div class="plan-head">Platinum Package</div>

    <div class="plan-label">Full SEO Audit</div>
    <div class="plan-cell">-</div><div class="plan-cell">-</div><div class="plan-cell">-</div>
    <div class="plan-cell"><svg width="24" height="20" viewBox="0 0 24 20" aria-label="Included"><path d="M2 11 L9 17 L22 2" fill="none" stroke="var(--tick)" stroke-width="2.5"/></svg></div>

    <div class="plan-label">LinkWheels</div>
    <div class="plan-cell alt">-</div><div class="plan-cell alt">-</div><div class="plan-cell alt">5 PR4 - PR7</div><div class="plan-cell alt">5 PR4 - PR7</div>

    <div class="plan-label">Social Bookmarks</div>
    <div class="plan-cell">10 PR3 - PR8</div><div class="plan-cell">10 PR3 - PR8</div><div class="plan-cell">10 PR3 - PR8</div><div class="plan-cell">10 PR3 - PR8</div>

    <div class="plan-label">Web 2.0 Profile Backlinks</div>
    <div class="plan-cell alt">15 PR5 - PR8</div><div class="plan-cell alt">15 PR5 - PR8</div><div class="plan-cell alt">15 PR5 - PR8</div><div class="plan-cell alt">45 PR5 - PR8</div>

    <div class="plan-label">EDU Backlinks</div>
    <div class="plan-cell">100</div><div class="plan-cell">100</div><div class="plan-cell">100</div><div class="plan-cell">100</div>

    <div class="plan-label">Backlinks</div>
    <div class="plan-cell alt">150 PR5 - PR7</div><div class="plan-cell alt">150 PR5 - PR7</div><div class="plan-cell alt">150 PR5 - PR7</div><div class="plan-cell alt">150 PR5 - PR7</div>

    <div class="plan-label">Profile Backlinks</div>
    <div class="plan-cell">-</div><div class="plan-cell">6000</div><div class="plan-cell">6000</div><div class="plan-cell">6000</div>

    <div class="plan-label">Blog Comments</div>
    <div class="plan-cell alt">-</div><div class="plan-cell alt">6000</div><div class="plan-cell alt">6000</div><div class="plan-cell alt">12000</div>

    <div class="plan-label">Wiki Backlinks</div>
    <div class="plan-cell">-</div><div class="plan-cell">-</div><div class="plan-cell">-</div><div class="plan-cell">1500</div>

    <div class="plan-label">Corvina</div>
    <div class="plan-cell alt">-</div><div class="plan-cell alt">-</div><div class="plan-cell alt">-</div><div class="plan-cell alt">280</div>

    <div class="plan-price-label">Price per month</div>
    <div class="plan-price">$ 39.00</div>
    <div class="plan-price">$ 58.00</div>
    <div class="plan-price">$ 79.00</div>
    <div class="plan-price">$ 139.00</div>
  </div>

  <svg class="back-to-top" viewBox="0 0 48 48" aria-label="Back to top">
    <circle cx="24" cy="24" r="24" fill="var(--top-btn)"/>
    <path d="M15 28 L24 19 L33 28" fill="none" stroke="#fff" stroke-width="3"/>
  </svg>
</section>
</body>
</html>
```